Business Card Design

I am starting my therapy private practice. I will be an in home therapist, so I go into family's homes instead of using an office to do family/marriage therapy. Therefore, I do not have an office address. I am looking for something in the black, red, gray, and blue color scheme that appeals to both families, couples and teenagers.

Industry/Entity Type

Business

Contact Information for Business Card

Lena Brightwell, MS, MFT Intern
Marriage and Family Therapy
In Home Therapist
617-482-5190
Lena@LenaBrightwell-example.com

```html
<!DOCTYPE html>
<html lang="en">
<head>
<meta charset="utf-8">
<title>Lena Brightwell – Business Card</title>
<link rel="stylesheet" href="https://fonts.googleapis.com/css2?family=Tinos:ital@0;1&family=Pinyon+Script&display=swap">
<style>
  :root {
    --slate-light: #46535b;
    --slate-dark: #232b31;
    --disc-light: #c9cdcf;
    --disc-mid: #80898d;
    --brand-teal: #4f7f8f;
    --text-white: #ffffff;
    --icon-red: #c4161c;
    --icon-red-light: #e8333a;
  }
  html, body {
    margin: 0;
    padding: 0;
    overflow: hidden;
    background: #ffffff;
  }
  .card {
    position: relative;
    width: 1200px;
    height: 686px;
    overflow: hidden;
    background: radial-gradient(ellipse at 60% 45%, var(--slate-light) 0%, var(--slate-dark) 85%);
    font-family: "Tinos", "Times New Roman", serif;
    color: var(--text-white);
  }
  .card__discs {
    position: absolute;
    inset: 0;
  }
  .brand {
    position: absolute;
    left: 90px;
    top: 150px;
    width: 320px;
    text-align: center;
    color: var(--brand-teal);
  }
  .brand__dot {
    display: block;
    width: 96px;
    height: 96px;
    margin: 0 auto 22px;
    border-radius: 50%;
    background: var(--brand-teal);
  }
  .brand__name {
    font-size: 36px;
    line-height: 1.1;
  }
  .identity {
    position: absolute;
    left: 612px;
    top: 300px;
  }
  .identity__name {
    margin: 0;
    font-size: 62px;
    font-weight: 400;
    line-height: 1;
    letter-spacing: 0.5px;
  }
  .identity__initial {
    font-family: "Pinyon Script", cursive;
    font-size: 76px;
    margin-right: 2px;
  }
  .identity__title {
    margin: 10px 0 0;
    font-style: italic;
    font-size: 22px;
    line-height: 33px;
  }
  .contact {
    position: absolute;
    left: 614px;
    top: 466px;
    margin: 0;
    padding: 0;
    list-style: none;
  }
  .contact__item {
    display: flex;
    align-items: center;
    height: 66px;
    margin-bottom: 8px;
    font-size: 27px;
  }
  .contact__icon {
    width: 66px;
    height: 66px;
    margin-right: 20px;
    flex: none;
  }
</style>
</head>
<body>
<main class="card">
  <svg class="card__discs" width="1200" height="686" viewBox="0 0 1200 686" aria-hidden="true">
    <defs>
      <radialGradient id="disc-back" cx="0.45" cy="0.35" r="0.7">
        <stop offset="0" stop-color="#9aa2a6"/>
        <stop offset="1" stop-color="var(--disc-mid)"/>
      </radialGradient>
      <radialGradient id="disc-front" cx="0.4" cy="0.4" r="0.7">
        <stop offset="0" stop-color="#d8dbdc"/>
        <stop offset="1" stop-color="#b9bec1"/>
      </radialGradient>
      <filter id="disc-shadow" x="-20%" y="-20%" width="140%" height="140%">
        <feDropShadow dx="4" dy="8" stdDeviation="12" flood-color="#000" flood-opacity="0.35"/>
      </filter>
    </defs>
    <circle cx="205" cy="290" r="395" fill="url(#disc-back)" filter="url(#disc-shadow)"/>
    <circle cx="240" cy="105" r="428" fill="url(#disc-front)" filter="url(#disc-shadow)"/>
  </svg>

  <div class="brand">
    <span class="brand__dot"></span>
    <div class="brand__name">Brightwell Therapy</div>
  </div>

  <section class="identity">
    <h1 class="identity__name"><span class="identity__initial">L</span>ena Brightwell</h1>
    <p class="identity__title">MS, MFT Intern Marriage and<br>Family Therapy In Home Therapist</p>
  </section>

  <ul class="contact">
    <li class="contact__item">
      <svg class="contact__icon" viewBox="0 0 66 66" aria-hidden="true">
        <defs>
          <linearGradient id="icon-red-a" x1="0" y1="0" x2="0" y2="1">
            <stop offset="0" stop-color="var(--icon-red-light)"/>
            <stop offset="1" stop-color="var(--icon-red)"/>
          </linearGradient>
        </defs>
        <rect x="1" y="1" width="64" height="64" rx="10" fill="url(#icon-red-a)"/>
        <path d="M14 26c0-6 8-10 19-10s19 4 19 10l-1 4h-9v-5c-3-1-6-1-9-1s-6 0-9 1v5h-9z" fill="#fff"/>
        <path d="M20 33l5-6h16l5 6v14H20z" fill="#fff"/>
        <circle cx="33" cy="39" r="5" fill="var(--icon-red)"/>
        <circle cx="33" cy="39" r="2.5" fill="#fff"/>
      </svg>
      <span>617-482-5190</span>
    </li>
    <li class="contact__item">
      <svg class="contact__icon" viewBox="0 0 66 66" aria-hidden="true">
        <defs>
          <linearGradient id="icon-red-b" x1="0" y1="0" x2="0" y2="1">
            <stop offset="0" stop-color="var(--icon-red-light)"/>
            <stop offset="1" stop-color="var(--icon-red)"/>
          </linearGradient>
        </defs>
        <rect x="1" y="1" width="64" height="64" rx="10" fill="url(#icon-red-b)"/>
        <rect x="12" y="19" width="42" height="28" fill="#fff"/>
        <path d="M12 19l21 16 21-16" fill="none" stroke="var(--icon-red)" stroke-width="3"/>
        <path d="M12 47l15-13M54 47L39 34" fill="none" stroke="var(--icon-red)" stroke-width="2"/>
      </svg>
      <span>Lena@LenaBrightwell-example.com</span>
    </li>
  </ul>
</main>
</body>
</html>
```